Corroway Medical Imaging marketing poster

A poster to advertise our services. Something outstanding that catches the eye. Will be displayed at medical centres. Needs to advertise the following:
Opening hours - Mon-fri 8am-5:30pm Sat 8am-12:30
Services offered: Ultrasound, CT, Xray, Conebeam CT, Barium Studies, Injections and Biopsies, 3D/4D pregnancy scans.
We Bulk Bill concession card holders and under 18's
Locally owned and operated
www.corrowaymedicalimaging.example.au
include contact details also Tel: 96384027 Fax: 9638 4093

```html
<!DOCTYPE html>
<html lang="en">
<head>
<meta charset="utf-8">
<title>Corroway Medical Imaging – Poster</title>
<link href="https://fonts.googleapis.com/css2?family=Tinos:wght@400;700&family=Open+Sans:wght@400;600;700&family=Oswald:wght@500&display=swap" rel="stylesheet">
<style>
  :root {
    --blue: #2ea3e3;
    --blue-deep: #1c8fd3;
    --green: #9cc31c;
    --green-dark: #86aa10;
    --ink: #1d1d1d;
    --grey-text: #4a4a4a;
    --paper: #f3f4f5;
    --paper-edge: #e2e4e6;
    --white: #ffffff;
  }
  * { box-sizing: border-box; margin: 0; padding: 0; }
  html, body { width: 848px; height: 1200px; overflow: hidden; }
  body { background: var(--paper); font-family: "Open Sans", Arial, sans-serif; }

  .poster {
    position: relative; width: 848px; height: 1200px; overflow: hidden;
    background: linear-gradient(160deg, var(--white) 0%, var(--paper) 45%, var(--paper-edge) 100%);
  }
  .poster__sheen {
    position: absolute; left: -120px; top: 520px; width: 1100px; height: 260px;
    background: linear-gradient(90deg, rgba(255,255,255,0) 0%, rgba(255,255,255,.8) 50%, rgba(255,255,255,0) 100%);
    transform: rotate(-22deg);
  }

  /* Brand */
  .brand { position: absolute; left: 44px; top: 58px; display: flex; align-items: center; gap: 16px; }
  .brand__dot { width: 40px; height: 40px; border-radius: 50%; background: var(--blue); }
  .brand__name {
    font-family: "Tinos", "Times New Roman", serif; color: var(--grey-text);
    font-weight: 400; line-height: 1; letter-spacing: 1px;
  }
  .brand__name span { display: block; }
  .brand__name .brand__line1 { font-size: 52px; }
  .brand__name .brand__line2 { font-size: 25px; margin-top: 6px; letter-spacing: 2px; }

  /* Photo circles */
  .photo-circle {
    position: absolute; border-radius: 50%;
    border: 14px solid var(--blue); background: var(--white); padding: 9px;
  }
  .photo-circle__inner {
    width: 100%; height: 100%; border-radius: 50%;
    border: 10px solid var(--green); overflow: hidden;
  }
  .photo-circle__fill { width: 100%; height: 100%; }
  .photo-circle--team { left: 37px; top: 219px; width: 524px; height: 524px; }
  .photo-circle--team .photo-circle__fill {
    background: radial-gradient(circle at 45% 60%, #2f8fd0 0%, #5aaee0 35%, #cfe3ee 70%, #eef3f5 100%);
  }
  .photo-circle--scan { left: 450px; top: 37px; width: 342px; height: 342px; border-width: 16px; }
  .photo-circle--scan .photo-circle__fill {
    background: linear-gradient(100deg, #f2eee9 0%, #e8e2dc 40%, #6a7580 70%, #2a323a 100%);
  }

  /* Hours */
  .hours {
    position: absolute; left: 560px; top: 345px; width: 210px; height: 210px; z-index: 2;
    border-radius: 50%; border: 9px solid var(--blue); background: var(--white); padding: 5px;
  }
  .hours__inner {
    width: 100%; height: 100%; border-radius: 50%; border: 5px solid var(--green);
    display: flex; flex-direction: column; align-items: center; justify-content: center;
    font-family: "Oswald", "Arial Narrow", sans-serif; text-align: center; line-height: 1.18;
  }
  .hours__title { font-size: 25px; color: var(--ink); }
  .hours__days { font-size: 24px; color: var(--green-dark); }
  .hours__time { font-size: 22px; color: var(--ink); font-family: "Open Sans", Arial, sans-serif; font-weight: 400; letter-spacing: -.5px; }
  .hours__time b { color: var(--green-dark); font-family: "Oswald", sans-serif; font-weight: 500; }

  /* Tagline */
  .tagline {
    position: absolute; left: 566px; top: 620px; width: 240px; text-align: center;
    font-family: "Tinos", "Times New Roman", serif; font-weight: 400; font-variant: small-caps;
    line-height: 1; white-space: nowrap;
  }
  .tagline span { display: block; }
  .tagline__a { color: var(--blue); font-size: 42px; letter-spacing: 1px; }
  .tagline__b { color: var(--green); font-size: 70px; margin-top: -6px; }
  .tagline__c { color: var(--ink); font-size: 31px; margin-top: -6px; }
  .tagline__d { color: var(--blue); font-size: 37px; margin-top: 0; }

  /* Contact */
  .contact { position: absolute; left: 58px; top: 800px; font-family: "Tinos", "Times New Roman", serif; line-height: 1; }
  .contact__label { font-size: 64px; color: var(--ink); letter-spacing: 1px; }
  .contact__tel { font-size: 60px; color: var(--blue-deep); margin-top: 14px; }
  .contact__fax { font-size: 40px; color: var(--green); font-variant: small-caps; margin-top: 10px; }

  /* Services */
  .services {
    position: absolute; left: 376px; top: 830px; width: 472px; height: 128px;
    border-radius: 22px 0 0 22px;
    background: linear-gradient(180deg, #7fd0f4 0%, var(--blue) 55%, var(--blue-deep) 100%);
    box-shadow: 0 4px 8px rgba(0,0,0,.15);
  }
  .services__tab {
    position: absolute; left: 286px; top: 6px; width: 152px; height: 30px; border-radius: 8px;
    background: linear-gradient(180deg, #c8e25a, var(--green)); color: var(--ink);
    font-weight: 700; font-size: 20px; text-align: center; line-height: 30px; letter-spacing: .5px;
  }
  .services__list {
    position: absolute; left: 0; top: 40px; width: 100%; display: flex;
    color: var(--white); font-weight: 600; font-size: 14px; line-height: 20px;
  }
  .services__col { list-style: none; padding: 0 10px; text-align: right; }
  .services__col + .services__col { border-left: 1px solid rgba(255,255,255,.6); }
  .services__col li::after {
    content: ""; display: inline-block; width: 6px; height: 6px; border-radius: 50%;
    background: var(--white); margin-left: 8px; vertical-align: middle;
  }
  .services__col li.no-dot::after { visibility: hidden; }
  .services__col--1 { width: 140px; }
  .services__col--2 { width: 140px; }
  .services__col--3 { width: 190px; }

  /* Footer */
  .notice {
    position: absolute; left: 0; top: 1014px; width: 848px; text-align: center;
    font-weight: 700; font-size: 17px; color: var(--ink);
  }
  .footer-wave { position: absolute; left: 0; top: 1040px; width: 848px; height: 160px; }
  .footer-url {
    position: absolute; left: 0; top: 1142px; width: 848px; text-align: center;
    color: var(--white); font-weight: 600; font-size: 22px; letter-spacing: .3px;
  }
</style>
</head>
<body>
<main class="poster">
  <div class="poster__sheen"></div>

  <header class="brand">
    <div class="brand__dot"></div>
    <div class="brand__name">
      <span class="brand__line1">CORROWAY</span>
      <span class="brand__line2">MEDICAL IMAGING</span>
    </div>
  </header>

  <div class="photo-circle photo-circle--team">
    <div class="photo-circle__inner">
      <div class="photo-circle__fill" role="img" aria-label="Photo of two smiling medical staff in blue scrubs with stethoscopes"></div>
    </div>
  </div>

  <div class="photo-circle photo-circle--scan">
    <div class="photo-circle__inner">
      <div class="photo-circle__fill" role="img" aria-label="Photo of a doctor examining a brain scan film"></div>
    </div>
  </div>

  <section class="hours">
    <div class="hours__inner">
      <div class="hours__title">Opening hours</div>
      <div class="hours__days">Mon-fri</div>
      <div class="hours__time">8am-5:30pm</div>
      <div class="hours__time"><b>Sat</b> 8am-12:30</div>
    </div>
  </section>

  <h2 class="tagline">
    <span class="tagline__a">Qualified</span>
    <span class="tagline__b">Staff</span>
    <span class="tagline__c">With Expertise</span>
    <span class="tagline__d">In Services</span>
  </h2>

  <section class="contact">
    <div class="contact__label">CALL US</div>
    <div class="contact__tel">96384027</div>
    <div class="contact__fax">Fax: 9638 4093</div>
  </section>

  <section class="services">
    <div class="services__tab">SERVICES:</div>
    <div class="services__list">
      <ul class="services__col services__col--1">
        <li>Ultrasound</li><li>CT</li><li>Xray</li>
      </ul>
      <ul class="services__col services__col--2">
        <li>Conebeam CT</li><li>Barium</li><li class="no-dot">Studies</li>
      </ul>
      <ul class="services__col services__col--3">
        <li>Injections and</li><li class="no-dot">Biopsies,</li><li>3D/4D pregnancy scans</li>
      </ul>
    </div>
  </section>

  <p class="notice">We Bulk Bill concession card holders and under 18's Locally owned and operated</p>

  <svg class="footer-wave" viewBox="0 0 848 160" preserveAspectRatio="none" aria-hidden="true">
    <defs>
      <linearGradient id="footerBlue" x1="0" y1="0" x2="0" y2="1">
        <stop offset="0" stop-color="#5bbdf0"/>
        <stop offset="1" stop-color="#2ea3e3"/>
      </linearGradient>
    </defs>
    <path d="M0 70 C 250 95, 560 70, 848 0 L848 160 L0 160 Z" fill="#9cc31c"/>
    <path d="M0 92 C 260 112, 560 88, 848 28 L848 160 L0 160 Z" fill="#ffffff"/>
    <path d="M0 102 C 260 122, 560 100, 848 44 L848 160 L0 160 Z" fill="url(#footerBlue)"/>
  </svg>
  <div class="footer-url">www.corrowaymedicalimaging.example.au</div>
</main>
</body>
</html>
```